Flyer-Design für Immobilienfirma
Zielgruppe
www.brenkholt-immobilien.de
Aufgabenstellung
Thema :
Neukunden generieren – Viele Wege führen zu neuen Leads ...
Sich selbst als Experten platzieren mit Bild
Dienstleistung : FÜR DEN IMMOBILIENBESITZER
Was ist Ihre Immobilie wert?
KOSTENLOSE Beratung durch Experten
KOSTENLOSE Immobilienbewertung
KOSTENLOS vorhandene Grundrisszeichnungen aktualisieren
KOSTENLOS 3D Grundrisszeichnungen und Ansicht
KOSTENLOS 3D Fotos und 360 Grad Ansichten
KOSTENLOS Drohnenaufnahmen IHRER Immobilien
KOSTENLOS Erstellung eines Energieverbrauchsausweises
evtl für die Rückseite
#Tippgeberprämie
Brenkholt & Partner Immobilien
so einfach verdienen Sie sich Ihre Tippprämie
wenn Sie Kenntnis vom beabsichtigten Verkauf einer Immobilie haben, dann setzen Sie sich mit uns in Verbindung.
Wir belohnen Ihren Tipp – wenn er zu einem Verkaufsabschluss durch uns führt –
mit 10 Prozent der an uns gezahlten Netto-Vermittlungsprovision (ohne MwSt.).
Dies gilt auch für Eigentümer, die uns Ihre Immobilie zum Verkauf geben.
Voraussetzungen für die Zahlung einer Tippgeber-Prämie sind:
Die Brenkholt & Partner immobilien kennt das angebotene Objekt noch nicht.
Das Objekt wird nicht bereits im Internet von dritter Seite beworben.
Die Brenkholt & Partner immobilien erhält die Erlaubnis zur Vermarktung der Immobilie.
Es kommt zu einem durch die Brenkholt & Partner immobilien vermittelten Verkauf
Sie erhalten Ihre Tippprämie unmittelbar nach Zahlung der Courtage an uns auf ein von Ihnen genanntes Konto überwiesen!

```html
<!DOCTYPE html>
<html lang="de">
<head>
<meta charset="utf-8">
<title>Für Eigentümer – Brenkholt &amp; Partner Real Estate</title>
<link rel="stylesheet" href="https://fonts.googleapis.com/css2?family=Outfit:wght@300;400&display=swap">
<style>
  :root {
    --gold: #d9ae52;
    --panel: #ececec;
    --text: #575757;
    --brand: #4a3d2f;
    --paper: #ffffff;
    --stage: #e6e6e6;
    --photo-expert: linear-gradient(165deg, #cfd3d6 0%, #9ea4a9 50%, #5f646a 100%);
    --photo-drone: linear-gradient(150deg, #7d8a5e 0%, #c9c7c4 40%, #a9a7a4 75%, #6f7470 100%);
    --photo-handshake: linear-gradient(170deg, #eef1f1 0%, #d9cfc0 55%, #a88f6c 100%);
  }
  html, body {
    margin: 0;
    width: 1200px;
    height: 1200px;
    overflow: hidden;
    background: var(--stage);
    font-family: "Outfit", sans-serif;
    font-weight: 300;
    color: var(--text);
  }
  .flyer {
    position: absolute;
    left: 229px;
    top: 76px;
    width: 741px;
    height: 1051px;
    background: var(--paper);
  }
  .brand {
    position: absolute;
    right: 71px;
    top: 70px;
    display: flex;
    align-items: center;
    gap: 8px;
    color: var(--brand);
    font-weight: 400;
    font-size: 15px;
  }
  .brand-mark {
    width: 12px;
    height: 12px;
    background: var(--gold);
  }
  .page-title {
    position: absolute;
    left: 24px;
    top: 168px;
    margin: 0;
    font-weight: 300;
    font-size: 39px;
    line-height: 48px;
    color: var(--text);
  }
  .offer {
    position: absolute;
    left: 0;
    width: 741px;
    height: 175px;
  }
  .offer-info {
    position: absolute;
    left: 0;
    top: 0;
    width: 333px;
    height: 175px;
    background: var(--panel);
    border-left: 23px solid var(--gold);
    box-sizing: border-box;
    padding: 14px 0 0 11px;
  }
  .offer-name {
    margin: 0 0 22px;
    font-weight: 300;
    font-size: 22px;
    line-height: 28px;
  }
  .offer-facts {
    margin: 0;
    font-size: 15.5px;
    line-height: 25px;
  }
  .offer-photo {
    position: absolute;
    left: 348px;
    top: 0;
    width: 393px;
    height: 175px;
  }
  .expert { top: 239px; }
  .expert .offer-photo { background: var(--photo-expert); }
  .services { top: 431px; }
  .services .offer-photo { background: var(--photo-drone); }
  .tip { top: 622px; }
  .tip .offer-photo { background: var(--photo-handshake); }
  .contact-call {
    position: absolute;
    left: 348px;
    top: 843px;
    margin: 0;
    font-size: 22px;
    line-height: 25px;
  }
  .footer-band {
    position: absolute;
    left: 25px;
    top: 975px;
    width: 716px;
    height: 75px;
    background: var(--gold);
    color: #fff;
    font-size: 15px;
    display: flex;
    align-items: center;
    justify-content: center;
    padding-top: 18px;
    box-sizing: border-box;
    gap: 9px;
  }
</style>
</head>
<body>
  <main class="flyer">
    <div class="brand"><span class="brand-mark"></span>Brenkholt &amp; Partner Real Estate</div>

    <h1 class="page-title">FÜR EIGENTÜMER</h1>

    <section class="offer expert">
      <div class="offer-info">
        <h2 class="offer-name">WAS IST IHRE IMMOBILIE WERT?</h2>
        <p class="offer-facts">KOSTENLOSE Beratung durch Experten<br>KOSTENLOSE Immobilienbewertung<br>Ihr persönlicher Ansprechpartner</p>
      </div>
      <div class="offer-photo" role="img" aria-label="Foto des Immobilienexperten im Anzug"></div>
    </section>

    <section class="offer services">
      <div class="offer-info">
        <h2 class="offer-name">KOSTENLOSE LEISTUNGEN</h2>
        <p class="offer-facts">Grundrisse aktualisieren, 3D Ansicht<br>3D Fotos und 360 Grad Ansichten<br>Drohnenaufnahmen, Energieausweis</p>
      </div>
      <div class="offer-photo" role="img" aria-label="Drohnenaufnahme einer Immobilie von oben"></div>
    </section>

    <section class="offer tip">
      <div class="offer-info">
        <h2 class="offer-name">#TIPPGEBERPRÄMIE</h2>
        <p class="offer-facts">10 % der Netto-Provision für Ihren Tipp<br>bei Verkaufsabschluss durch uns<br>auch für Eigentümer</p>
      </div>
      <div class="offer-photo" role="img" aria-label="Foto einer Schlüsselübergabe vor einem Haus"></div>
    </section>

    <p class="contact-call">Interesse?<br>+49 (0) 421 55 30 12 48-20</p>

    <footer class="footer-band">
      <span>www.brenkholt-immobilien.de</span><span>|</span><span>contact@brenkholt-immobilien.de</span>
    </footer>
  </main>
</body>
</html>
```